Looking for a professional, clean and crisp business card

I am in the underground utilities industry and am just looking for a really impressive business card. I would like our card to be white with our symbol crisp and clear with it protruding. I also have a business partner that will require his name and info on the card once the design is set. I would like to have our website info on the card which is;
http://granitetrenchco.example/

Contact Information for Business Card

Website, contact name, number and email

```html
<!DOCTYPE html>
<html lang="en">
<head>
<meta charset="utf-8">
<title>Granite Trench Co — Business Card</title>
<link href="https://fonts.googleapis.com/css2?family=Roboto+Condensed:wght@400;700&display=swap" rel="stylesheet">
<style>
  :root {
    --page: #e9e8e6;
    --brand-blue: #3b62a8;
    --ink: #1b1b1d;
    --paper: #ffffff;
    --rule: #9a9a9a;
    --white: #ffffff;
  }
  * { box-sizing: border-box; margin: 0; padding: 0; }
  html, body { width: 1200px; height: 960px; overflow: hidden; }
  body {
    background: var(--page);
    font-family: "Roboto Condensed", "Arial Narrow", sans-serif;
    display: flex;
    flex-direction: column;
    align-items: center;
    justify-content: center;
    gap: 64px;
  }
  .card {
    position: relative;
    width: 600px;
    height: 343px;
    overflow: hidden;
    box-shadow: 0 2px 10px rgba(0,0,0,0.12);
  }

  /* Front */
  .card-front { background: var(--brand-blue); }
  .card-front .brand {
    position: absolute;
    top: 110px; left: 0; right: 0;
    display: flex; align-items: center; justify-content: center; gap: 14px;
  }
  .brand-dot {
    width: 26px; height: 26px; border-radius: 50%;
    background: var(--white);
  }
  .card-front .brand-name {
    color: var(--white);
    font-weight: 700;
    font-size: 40px;
    letter-spacing: 2px;
    text-transform: uppercase;
  }
  .card-front .website {
    position: absolute;
    bottom: 58px; left: 0; right: 0;
    text-align: center;
    color: var(--white);
    font-size: 15px;
    letter-spacing: 1.5px;
  }

  /* Back */
  .card-back { background: var(--paper); }
  .card-back .brand {
    position: absolute;
    top: 58px; left: 0; right: 0;
    display: flex; align-items: center; justify-content: center; gap: 12px;
  }
  .card-back .brand-dot { background: var(--brand-blue); width: 22px; height: 22px; }
  .card-back .brand-name {
    color: var(--ink);
    font-weight: 700;
    font-size: 32px;
    letter-spacing: 2px;
    text-transform: uppercase;
  }
  .person {
    position: absolute;
    top: 196px; right: 320px;
    text-align: left;
  }
  .person-name {
    color: var(--ink);
    font-weight: 700;
    font-size: 17px;
    letter-spacing: 0.5px;
    text-transform: uppercase;
  }
  .person-title {
    color: var(--brand-blue);
    font-size: 12px;
    letter-spacing: 0.5px;
    text-transform: uppercase;
    margin-top: 2px;
  }
  .divider {
    position: absolute;
    top: 150px; left: 300px;
    width: 1px; height: 90px;
    background: var(--rule);
  }
  .contact-list {
    position: absolute;
    top: 152px; left: 322px;
    list-style: none;
    display: flex; flex-direction: column; gap: 12px;
  }
  .contact-list li {
    display: flex; align-items: center; gap: 10px;
    color: var(--ink);
    font-size: 12.5px;
    letter-spacing: 0.4px;
    text-transform: uppercase;
  }
  .contact-icon {
    width: 18px; height: 18px;
    background: var(--brand-blue);
    display: flex; align-items: center; justify-content: center;
  }
  .band-blue {
    position: absolute; left: 0; bottom: 0;
    width: 56%; height: 14px;
    background: var(--brand-blue);
  }
  .band-black {
    position: absolute; right: 0; bottom: 0;
    width: 44%; height: 18px;
    background: var(--ink);
  }
</style>
</head>
<body>

  <section class="card card-front" aria-label="Card front">
    <div class="brand">
      <span class="brand-dot"></span>
      <span class="brand-name">Granite Trench Co</span>
    </div>
    <p class="website">WWW.GRANITETRENCHCO.EXAMPLE</p>
  </section>

  <section class="card card-back" aria-label="Card back">
    <div class="brand">
      <span class="brand-dot"></span>
      <span class="brand-name">Granite Trench Co</span>
    </div>

    <div class="person">
      <p class="person-name">Dale Marrick</p>
      <p class="person-title">Owner</p>
    </div>

    <div class="divider"></div>

    <ul class="contact-list">
      <li>
        <span class="contact-icon">
          <svg width="12" height="12" viewBox="0 0 24 24" aria-hidden="true"><path fill="#fff" d="M6.6 10.8a15.1 15.1 0 0 0 6.6 6.6l2.2-2.2c.3-.3.7-.4 1-.2 1.1.4 2.3.6 3.6.6.6 0 1 .4 1 1V20c0 .6-.4 1-1 1C10.6 21 3 13.4 3 4c0-.6.4-1 1-1h3.5c.6 0 1 .4 1 1 0 1.3.2 2.5.6 3.6.1.3 0 .7-.2 1z"/></svg>
        </span>
        555-014-2286
      </li>
      <li>
        <span class="contact-icon">
          <svg width="12" height="12" viewBox="0 0 24 24" aria-hidden="true"><path fill="#fff" d="M3 5h18v14H3z"/><path fill="none" stroke="#3b62a8" stroke-width="2" d="M3 6l9 7 9-7"/></svg>
        </span>
        dale@granitetrenchco.example
      </li>
      <li>
        <span class="contact-icon">
          <svg width="12" height="12" viewBox="0 0 24 24" aria-hidden="true"><g fill="none" stroke="#fff" stroke-width="2"><circle cx="12" cy="12" r="9"/><ellipse cx="12" cy="12" rx="4" ry="9"/><path d="M3 12h18"/></g></svg>
        </span>
        www.granitetrenchco.example
      </li>
    </ul>

    <div class="band-blue"></div>
    <div class="band-black"></div>
  </section>

</body>
</html>
```